Build Your Own Shake Menu Design

Menu Design
- will be printed on countertop acrylic menu stands that are a foot by a foot

Files:
- document attached for the menu contents
*file name: SHAKEMENU
- sample menu images (these are giant acrylic menu boards that are in my shop)
*file name: newest shave ice menu, newest spi rolls menu (JPG)
-picture of the shop where the menus will be placed
*file name: shop (PNG)

```html
<!DOCTYPE html>
<html lang="en">
<head>
<meta charset="utf-8">
<title>Create Your Own Shake Menu</title>
<link rel="stylesheet" href="https://fonts.googleapis.com/css2?family=Montserrat:wght@700;800&family=Roboto:wght@400;500;700&display=swap">
<style>
  :root {
    --stage: #ababab;
    --red: #c8202f;
    --light-bg: #f0f0f1;
    --light-ink: #1e1e20;
    --light-muted: #5c5c60;
    --dark-bg: #1d1c1e;
    --dark-ink: #ffffff;
    --dark-muted: #f2f2f2;
    --board: #161517;
  }
  * { box-sizing: border-box; margin: 0; padding: 0; }
  html, body { width: 732px; height: 1200px; overflow: hidden; }
  body { background: var(--stage); position: relative; font-family: "Roboto", Arial, sans-serif; }

  .menu {
    position: absolute; left: 56px; width: 620px; height: 517px; overflow: hidden;
    background: var(--bg); color: var(--ink);
    box-shadow: 0 1px 4px rgba(0,0,0,.25);
  }
  .menu--light { top: 59px; --bg: var(--light-bg); --ink: var(--light-ink); --muted: var(--light-muted); --ring: var(--red); }
  .menu--dark { top: 623px; --bg: var(--dark-bg); --ink: var(--dark-ink); --muted: var(--dark-muted); --ring: #ffffff; }

  .hero { position: absolute; left: 0; top: 0; width: 620px; height: 240px; }

  .heading {
    position: absolute; left: 20px; font-family: "Montserrat", Arial, sans-serif; font-weight: 700;
    font-size: 8.8px; letter-spacing: 0; line-height: 12.4px; text-transform: uppercase;
  }
  .heading--intro { top: 250px; }
  .heading--base { top: 271px; }
  .heading--standard { top: 292px; }
  .heading--specialty { top: 412px; }
  .heading--flavours { top: 435px; }
  .heading--items { top: 469px; }

  .base-list { position: absolute; left: 20px; top: 320px; width: 220px; list-style: none; }
  .base-list li {
    position: relative; height: 19.5px; padding-left: 16px; font-size: 7.6px; line-height: 14px;
    color: var(--muted);
  }
  .base-list .price { position: absolute; left: 141px; top: 0; font-weight: 700; color: var(--ink); }
  .bullet { position: absolute; left: 0; top: 3px; width: 7px; height: 7px; }

  .drink-board {
    position: absolute; left: 230px; top: 281px; width: 160px; height: 210px;
    background: var(--board); border: 3px solid var(--red); border-radius: 10px;
  }
  .drink-list { position: absolute; left: 13px; right: 13px; top: 44px; list-style: none; color: #fff; }
  .drink-list li {
    display: flex; justify-content: space-between; align-items: center;
    font-size: 12.5px; line-height: 15px; height: 26.2px; letter-spacing: .2px;
  }
  .drink-list li.two-line { height: 36px; line-height: 18px; margin-top: 4px; align-items: flex-end; }
  .drink-list .price { font-weight: 700; }
  .scoop-photo { position: absolute; left: 271px; top: 243px; width: 78px; height: 78px; }

  .additions-title {
    position: absolute; left: 416px; top: 246px; width: 200px;
    font-family: "Montserrat", Arial, sans-serif; font-weight: 700; font-size: 13.6px; line-height: 16.6px;
  }
  .additions-text {
    position: absolute; left: 416px; top: 289px; width: 184px;
    font-size: 7px; line-height: 12.4px; text-align: justify; font-weight: 500;
  }
  .spoon-notes { position: absolute; left: 416px; top: 401px; width: 184px; list-style: none; }
  .spoon-notes li {
    position: relative; padding-left: 15px; font-size: 7px; line-height: 10.2px;
    color: var(--muted); margin-bottom: 5.6px;
  }
  .spoon-notes .bullet { top: 1.6px; left: 0; }
</style>
</head>
<body>

<!-- Light edition -->
<section class="menu menu--light">
  <svg class="hero" viewBox="0 0 620 240">
    <defs>
      <linearGradient id="photoLight" x1="0" y1="0" x2="1" y2="1">
        <stop offset="0" stop-color="#6b4b44"/>
        <stop offset=".5" stop-color="#4a302b"/>
        <stop offset="1" stop-color="#2e1e1b"/>
      </linearGradient>
      <radialGradient id="oatLight" cx=".45" cy=".45" r=".6">
        <stop offset="0" stop-color="#efe6d8"/>
        <stop offset="1" stop-color="#cdbfa9"/>
      </radialGradient>
    </defs>
    <path d="M0,0 H620 V168 C540,212 460,236 382,236 C300,236 230,207 160,172 L0,12 Z" fill="var(--red)"/>
    <path d="M0,0 H620 V141 C540,190 460,222 382,222 C300,222 230,196 165,160 L56,78 L0,10 Z" fill="url(#photoLight)" role="img" aria-label="Chocolate milkshake with whipped cream and a striped straw on a wooden board with cinnamon sticks and cocoa powder"/>
    <circle cx="98" cy="144" r="77" fill="var(--ring)"/>
    <circle cx="98" cy="144" r="72.5" fill="url(#oatLight)" role="img" aria-label="Oat and banana smoothie in a glass with a spoon of chia seeds"/>
  </svg>

  <h2 class="heading heading--intro">Create your own shake menu</h2>
  <h2 class="heading heading--base">Choose your base</h2>
  <h2 class="heading heading--standard">Standard base- Van - Chocolate</h2>

  <ul class="base-list">
    <li><svg class="bullet" viewBox="0 0 10 10"><circle cx="5" cy="5" r="5" fill="var(--red)"/><path d="M2.3 5h4.4M4.8 3 6.8 5 4.8 7" stroke="#fff" stroke-width="1.4" fill="none"/></svg>15 ounce Regular<span class="price">$5.75</span></li>
    <li><svg class="bullet" viewBox="0 0 10 10"><circle cx="5" cy="5" r="5" fill="var(--red)"/><path d="M2.3 5h4.4M4.8 3 6.8 5 4.8 7" stroke="#fff" stroke-width="1.4" fill="none"/></svg>15 ounce Specialty Base<span class="price">$6.25</span></li>
    <li><svg class="bullet" viewBox="0 0 10 10"><circle cx="5" cy="5" r="5" fill="var(--red)"/><path d="M2.3 5h4.4M4.8 3 6.8 5 4.8 7" stroke="#fff" stroke-width="1.4" fill="none"/></svg>18 ounce Large<span class="price">$5.99</span></li>
    <li><svg class="bullet" viewBox="0 0 10 10"><circle cx="5" cy="5" r="5" fill="var(--red)"/><path d="M2.3 5h4.4M4.8 3 6.8 5 4.8 7" stroke="#fff" stroke-width="1.4" fill="none"/></svg>18 ounce Specialty Base<span class="price">$6.49</span></li>
  </ul>

  <h2 class="heading heading--specialty">Specialty bases</h2>
  <h2 class="heading heading--flavours">Mint-Strawberry-Espresso<br>Cheesecake</h2>
  <h2 class="heading heading--items">Choose up to 2 items for your<br>shake</h2>

  <div class="drink-board">
    <ul class="drink-list">
      <li><span>Water</span><span class="price">$1.00</span></li>
      <li><span>Cola</span><span class="price">$1.99</span></li>
      <li><span>Lemon-Lime</span><span class="price">$1.99</span></li>
      <li><span>Tea</span><span class="price">$1.99</span></li>
      <li class="two-line"><span>Sports Drink<br>Fruit Punch</span><span class="price">$1.99</span></li>
    </ul>
  </div>
  <svg class="scoop-photo" viewBox="0 0 78 78">
    <defs>
      <radialGradient id="scoopLight" cx=".5" cy=".55" r=".6">
        <stop offset="0" stop-color="#f4efe6"/>
        <stop offset=".6" stop-color="#c9a58f"/>
        <stop offset="1" stop-color="#7d3b3a"/>
      </radialGradient>
    </defs>
    <circle cx="39" cy="39" r="39" fill="var(--red)"/>
    <circle cx="39" cy="39" r="35.5" fill="url(#scoopLight)" role="img" aria-label="Vanilla ice cream scoops with strawberries and blueberries in a bowl"/>
  </svg>

  <h2 class="additions-title">LIST OF ADDITIONS TO CHOOSE FROM</h2>
  <p class="additions-text">Cookie Dough - Peanut Butter Cup - Butter Crunch - Mint Thins - Toffee Bits - Choc Chip Cookies - Graham Crackers - Cream Cookies - Chocolate Chips - White Chocolate Chips - Rainbow Sprinkles - Cupcake Bites - Candy Buttons - Nuts - Almonds - Strawberries - Banana - Cherries - Corn Crunch - Cinnamon Squares - Fruity Flakes - Cocoa Flakes - Peanut Butter Drizzle - Chocolate Drizzle - Strawberry Drizzle - Raspberry Drizzle - Marshmallow Drizzle</p>

  <ul class="spoon-notes">
    <li><svg class="bullet" viewBox="0 0 10 10"><circle cx="5" cy="5" r="5" fill="var(--red)"/><path d="M2.3 5h4.4M4.8 3 6.8 5 4.8 7" stroke="#fff" stroke-width="1.4" fill="none"/></svg>Its for our Color Changing Spoons</li>
    <li><svg class="bullet" viewBox="0 0 10 10"><circle cx="5" cy="5" r="5" fill="var(--red)"/><path d="M2.3 5h4.4M4.8 3 6.8 5 4.8 7" stroke="#fff" stroke-width="1.4" fill="none"/></svg>Color Changing Spoons are .50 cents and come in 3 colors</li>
    <li><svg class="bullet" viewBox="0 0 10 10"><circle cx="5" cy="5" r="5" fill="var(--red)"/><path d="M2.3 5h4.4M4.8 3 6.8 5 4.8 7" stroke="#fff" stroke-width="1.4" fill="none"/></svg>White to Blue -Pink to Purple- White to Confetti</li>
    <li><svg class="bullet" viewBox="0 0 10 10"><circle cx="5" cy="5" r="5" fill="var(--red)"/><path d="M2.3 5h4.4M4.8 3 6.8 5 4.8 7" stroke="#fff" stroke-width="1.4" fill="none"/></svg>Im hoping for some kind of image for them so kids can tell what they are</li>
    <li><svg class="bullet" viewBox="0 0 10 10"><circle cx="5" cy="5" r="5" fill="var(--red)"/><path d="M2.3 5h4.4M4.8 3 6.8 5 4.8 7" stroke="#fff" stroke-width="1.4" fill="none"/></svg>Same thing for the drinks, the visuals help.</li>
  </ul>
</section>

<!-- Dark edition -->
<section class="menu menu--dark">
  <svg class="hero" viewBox="0 0 620 240">
    <defs>
      <linearGradient id="photoDark" x1="0" y1="0" x2="1" y2="1">
        <stop offset="0" stop-color="#6b4b44"/>
        <stop offset=".5" stop-color="#4a302b"/>
        <stop offset="1" stop-color="#2e1e1b"/>
      </linearGradient>
      <radialGradient id="bowlDark" cx=".5" cy=".5" r=".6">
        <stop offset="0" stop-color="#b985c4"/>
        <stop offset=".55" stop-color="#9a6aa8"/>
        <stop offset="1" stop-color="#4a3128"/>
      </radialGradient>
    </defs>
    <path d="M0,0 H620 V168 C540,212 460,236 382,236 C300,236 230,207 160,172 L0,12 Z" fill="var(--red)"/>
    <path d="M0,0 H620 V153 C540,200 460,229 382,229 C300,229 230,202 162,166 L0,11 Z" fill="#ffffff"/>
    <path d="M0,0 H620 V141 C540,190 460,220 382,220 C300,220 230,194 165,158 L56,78 L0,10 Z" fill="url(#photoDark)" role="img" aria-label="Chocolate milkshake with whipped cream and a striped straw on a wooden board with cinnamon sticks and cocoa powder"/>
    <circle cx="98" cy="144" r="77" fill="var(--ring)"/>
    <circle cx="98" cy="144" r="72.5" fill="url(#bowlDark)" role="img" aria-label="Berry smoothie bowl topped with blueberries, granola and chia seeds on a wooden table"/>
  </svg>

  <h2 class="heading heading--intro">Create your own shake menu</h2>
  <h2 class="heading heading--base">Choose your base</h2>
  <h2 class="heading heading--standard">Standard base- Van - Chocolate</h2>

  <ul class="base-list">
    <li><svg class="bullet" viewBox="0 0 10 10"><circle cx="5" cy="5" r="5" fill="var(--red)"/><path d="M2.3 5h4.4M4.8 3 6.8 5 4.8 7" stroke="#fff" stroke-width="1.4" fill="none"/></svg>15 ounce Regular<span class="price">$5.75</span></li>
    <li><svg class="bullet" viewBox="0 0 10 10"><circle cx="5" cy="5" r="5" fill="var(--red)"/><path d="M2.3 5h4.4M4.8 3 6.8 5 4.8 7" stroke="#fff" stroke-width="1.4" fill="none"/></svg>15 ounce Specialty Base<span class="price">$6.25</span></li>
    <li><svg class="bullet" viewBox="0 0 10 10"><circle cx="5" cy="5" r="5" fill="var(--red)"/><path d="M2.3 5h4.4M4.8 3 6.8 5 4.8 7" stroke="#fff" stroke-width="1.4" fill="none"/></svg>18 ounce Large<span class="price">$5.99</span></li>
    <li><svg class="bullet" viewBox="0 0 10 10"><circle cx="5" cy="5" r="5" fill="var(--red)"/><path d="M2.3 5h4.4M4.8 3 6.8 5 4.8 7" stroke="#fff" stroke-width="1.4" fill="none"/></svg>18 ounce Specialty Base<span class="price">$6.49</span></li>
  </ul>

  <h2 class="heading heading--specialty">Specialty bases</h2>
  <h2 class="heading heading--flavours">Mint-Strawberry-Espresso<br>Cheesecake</h2>
  <h2 class="heading heading--items">Choose up to 2 items for your<br>shake</h2>

  <div class="drink-board">
    <ul class="drink-list">
      <li><span>Water</span><span class="price">$1.00</span></li>
      <li><span>Cola</span><span class="price">$1.99</span></li>
      <li><span>Lemon-Lime</span><span class="price">$1.99</span></li>
      <li><span>Tea</span><span class="price">$1.99</span></li>
      <li class="two-line"><span>Sports Drink<br>Fruit Punch</span><span class="price">$1.99</span></li>
    </ul>
  </div>
  <svg class="scoop-photo" viewBox="0 0 78 78">
    <defs>
      <radialGradient id="scoopDark" cx=".5" cy=".55" r=".6">
        <stop offset="0" stop-color="#f4efe6"/>
        <stop offset=".6" stop-color="#c9a58f"/>
        <stop offset="1" stop-color="#7d3b3a"/>
      </radialGradient>
    </defs>
    <circle cx="39" cy="39" r="39" fill="var(--red)"/>
    <circle cx="39" cy="39" r="35.5" fill="url(#scoopDark)" role="img" aria-label="Vanilla ice cream scoops with strawberries and blueberries in a bowl"/>
  </svg>

  <h2 class="additions-title">LIST OF ADDITIONS TO CHOOSE FROM</h2>
  <p class="additions-text">Cookie Dough - Peanut Butter Cup - Butter Crunch - Mint Thins - Toffee Bits - Choc Chip Cookies - Graham Crackers - Cream Cookies - Chocolate Chips - White Chocolate Chips - Rainbow Sprinkles - Cupcake Bites - Candy Buttons - Nuts - Almonds - Strawberries - Banana - Cherries - Corn Crunch - Cinnamon Squares - Fruity Flakes - Cocoa Flakes - Peanut Butter Drizzle - Chocolate Drizzle - Strawberry Drizzle - Raspberry Drizzle - Marshmallow Drizzle</p>

  <ul class="spoon-notes">
    <li><svg class="bullet" viewBox="0 0 10 10"><circle cx="5" cy="5" r="5" fill="var(--red)"/><path d="M2.3 5h4.4M4.8 3 6.8 5 4.8 7" stroke="#fff" stroke-width="1.4" fill="none"/></svg>Its for our Color Changing Spoons</li>
    <li><svg class="bullet" viewBox="0 0 10 10"><circle cx="5" cy="5" r="5" fill="var(--red)"/><path d="M2.3 5h4.4M4.8 3 6.8 5 4.8 7" stroke="#fff" stroke-width="1.4" fill="none"/></svg>Color Changing Spoons are .50 cents and come in 3 colors</li>
    <li><svg class="bullet" viewBox="0 0 10 10"><circle cx="5" cy="5" r="5" fill="var(--red)"/><path d="M2.3 5h4.4M4.8 3 6.8 5 4.8 7" stroke="#fff" stroke-width="1.4" fill="none"/></svg>White to Blue -Pink to Purple- White to Confetti</li>
    <li><svg class="bullet" viewBox="0 0 10 10"><circle cx="5" cy="5" r="5" fill="var(--red)"/><path d="M2.3 5h4.4M4.8 3 6.8 5 4.8 7" stroke="#fff" stroke-width="1.4" fill="none"/></svg>Im hoping for some kind of image for them so kids can tell what they are</li>
    <li><svg class="bullet" viewBox="0 0 10 10"><circle cx="5" cy="5" r="5" fill="var(--red)"/><path d="M2.3 5h4.4M4.8 3 6.8 5 4.8 7" stroke="#fff" stroke-width="1.4" fill="none"/></svg>Same thing for the drinks, the visuals help.</li>
  </ul>
</section>

</body>
</html>
```